Feral Horizon, a 3d voxel survival video game needs a card for gaming conventions

I am the lead developer for Feral Horizon http://www.FeralHorizon.example and need a business card to hand out at an indie gaming convention
The card would need to include the game name, website url, my name, position (Lead Developer), e-mail and phone number
The game is a 3d, voxel (with smooth terrain) based survival game with guns and wildlife. The main icon of the game would likely be a grizzly bear but I am willing to accept other designs too.
Attached is a media kit for the game with some images you can use but don't have to its just what little art I can provide. Anything on the website or from the video game can also be used. unrelated art can also be used.
Target Market(s)
Indie Developers/publishers at conferences
Industry/Entity Type
Games
Contact Information for Business Card
Name: Corwin Aldersby
Position: Lead Developer
E-mail: Pale_Lanterns@mailbox.example
Phone number: 555-207-3186

```html
<!DOCTYPE html>
<html lang="en">
<head>
<meta charset="utf-8">
<title>Feral Horizon – Business Card</title>
<link rel="stylesheet" href="https://fonts.googleapis.com/css2?family=Roboto:wght@400&family=Saira+Semi+Condensed:wght@600;700&display=swap">
<style>
  :root {
    --backdrop: #aeabab;
    --olive-light: #d8d1b2;
    --olive-mid: #8f8a63;
    --olive-dark: #3b3a1f;
    --card-black: #1f1f1f;
    --brand-red: #9c1b17;
    --stripe-khaki: #a39b78;
    --logo-rust: #8e3326;
    --header-khaki: #b7a57a;
    --text-white: #ffffff;
    --text-soft: #e2e2e2;
    --bear-light: #a77a55;
    --bear-dark: #5a3a22;
  }
  * { margin: 0; padding: 0; box-sizing: border-box; }
  html, body { width: 1200px; height: 1200px; overflow: hidden; }
  body { background: var(--backdrop); position: relative; font-family: "Roboto", sans-serif; }

  .card { position: absolute; width: 714px; height: 420px; overflow: hidden; }

  /* Front */
  .card--front {
    left: 237px; top: 118px;
    background: radial-gradient(ellipse 60% 62% at 50% 52%, var(--olive-light) 0%, var(--olive-mid) 60%, var(--olive-dark) 100%);
  }
  .front__emblem-photo {
    position: absolute; left: 233px; top: 62px; width: 145px; height: 160px;
    background: radial-gradient(ellipse at 50% 40%, var(--bear-light) 0%, var(--bear-dark) 70%, rgba(90,58,34,0) 100%);
    border-radius: 45% 45% 20% 20%;
  }
  .front__wordmark {
    position: absolute; left: 0; width: 100%; top: 226px; text-align: center;
    font-family: "Saira Semi Condensed", sans-serif; font-weight: 700;
    font-size: 58px; line-height: 54px; letter-spacing: 3px;
    color: var(--logo-rust); text-transform: uppercase;
  }

  /* Back */
  .card--back { left: 229px; top: 643px; height: 422px; background: var(--card-black); }
  .back__waves { position: absolute; inset: 0; }
  .back__bear-photo {
    position: absolute; left: 0; top: 105px; width: 185px; height: 317px;
    background: linear-gradient(160deg, var(--bear-light) 0%, var(--bear-dark) 75%, #c9c4bc 100%);
    border-radius: 40% 30% 0 0;
  }
  .back__wordmark {
    position: absolute; right: 36px; top: 36px;
    font-family: "Saira Semi Condensed", sans-serif; font-weight: 700;
    font-size: 44px; letter-spacing: 4px; line-height: 1;
    color: var(--header-khaki); text-transform: uppercase;
  }
  .back__person { position: absolute; right: 37px; top: 126px; text-align: right; }
  .back__name {
    font-family: "Saira Semi Condensed", sans-serif; font-weight: 600;
    font-size: 27px; color: var(--text-white); line-height: 1.1;
  }
  .back__role { font-size: 16px; color: var(--text-soft); margin-top: 6px; }

  .back__contact { position: absolute; right: 31px; top: 308px; list-style: none; }
  .back__contact li {
    display: flex; justify-content: flex-end; align-items: center; gap: 12px;
    font-size: 17px; color: var(--text-white); height: 27px;
  }
  .back__contact svg { width: 16px; height: 16px; flex: none; }
</style>
</head>
<body>

  <section class="card card--front" aria-label="Card front">
    <div class="front__emblem-photo" role="img" aria-label="Photo of a roaring grizzly bear"></div>
    <div class="front__wordmark">Feral<br>Horizon</div>
  </section>

  <section class="card card--back" aria-label="Card back">
    <svg class="back__waves" viewBox="0 0 714 422" width="714" height="422" aria-hidden="true">
      <path d="M0,352 C160,330 300,270 460,245 C570,228 650,222 714,218 L714,228 C640,232 560,240 470,256 C320,284 170,340 0,364 Z" fill="var(--stripe-khaki)"/>
      <path d="M0,372 C170,352 320,300 480,272 C590,254 660,248 714,244 L714,250 C650,254 580,262 485,280 C330,310 180,362 0,380 Z" fill="var(--stripe-khaki)" opacity="0.8"/>
      <path d="M180,422 C290,345 430,300 560,280 C630,268 680,262 714,258 L714,422 Z" fill="var(--brand-red)"/>
    </svg>

    <div class="back__bear-photo" role="img" aria-label="Photo of a grizzly bear standing on a rock"></div>

    <div class="back__wordmark">Feral Horizon</div>

    <div class="back__person">
      <div class="back__name">Corwin Aldersby</div>
      <div class="back__role">Lead Developer</div>
    </div>

    <ul class="back__contact">
      <li>555-207-3186
        <svg viewBox="0 0 16 16"><path d="M2 6 C2 3 14 3 14 6 L11 7 L10 5 H6 L5 7 Z M4 8 H12 L13 13 H3 Z" fill="var(--text-white)"/></svg>
      </li>
      <li>www.feralhorizon.example
        <svg viewBox="0 0 16 16"><rect x="1.5" y="3.5" width="13" height="9" fill="none" stroke="var(--text-white)" stroke-width="1.5"/><path d="M1.5 3.5 L8 9 L14.5 3.5" fill="none" stroke="var(--text-white)" stroke-width="1.5"/></svg>
      </li>
      <li>Pale_Lanterns@mailbox.example
        <svg viewBox="0 0 16 16"><circle cx="8" cy="8" r="6.2" fill="none" stroke="var(--text-white)" stroke-width="1.3"/><ellipse cx="8" cy="8" rx="2.6" ry="6.2" fill="none" stroke="var(--text-white)" stroke-width="1.1"/><path d="M2 8 H14" stroke="var(--text-white)" stroke-width="1.1"/></svg>
      </li>
    </ul>
  </section>

</body>
</html>
```